Valtera Drones webdesign: Innovative Drones service company in agriculture

We need a new website according the following conditions:
• Main colour orange and current logo;
• Transparent – open – trustworthy – dynamic - personal;
• Use the smartness and overview characteristics of the crow (Valtera is Latin for crow);
• Accessible to multiple target groups and markets:
o So not too horticultural, too green;
• Use contradictions:
o Future versus nostalgia;
o Smartness crow versus precision hummingbird;
o Technology versus mechanical;
• Kestam 2.4 GTR as a style icon?
• Long pager website
Updates

Website menu o Home o Crop monitoring  Applications Growth | Stress | Development | Diseases  Markets Breeding | Young plant | Potplants | Cutflowers | Vegetables | Soft fruit  Customer cases o Technology Aerial data collection | Artificial intelligence | Free data sets o About Vision | Company | Partners | Team | Career o Contact o News&downloads Logo: www.valteradrones-example.com

Target Market(s)

agriculture: owners, crop managers
oil&gas: maintenance, quality control managers and purchase managers
logistics: ware house managers, purchase managers

Industry/Entity Type

Agribusiness

Number of Pages Required

2 page

Colors
f78f20

Requirements
Must have
• long pager website
downloads
plain circle
Should not have
• Not too 'green' because first impression of designers of agriculture/horticulture is using the green colour. But that is not necessary.

Keep in mind that the current logo will be updates: the circle will be more 'general' and less 'agri'. Also the green colors in the logo will be slightly darker to make it more powerful.

```html
<!DOCTYPE html>
<html lang="en">
<head>
<meta charset="utf-8">
<title>Valtera Drones</title>
<link href="https://fonts.googleapis.com/css2?family=Rajdhani:wght@600;700&family=Lato:wght@400;700&display=swap" rel="stylesheet">
<style>
:root{
  --orange:#f78f20;
  --green:#237a27;
  --ink:#1e1e1e;
  --text:#3a3a3a;
  --muted:#8a8a8a;
  --soft:#f4f4f4;
  --line:#e2e2e2;
  --dark:#1b1b1b;
  --white:#ffffff;
}
*{margin:0;padding:0;box-sizing:border-box}
html,body{width:1200px;height:4694px;overflow:hidden}
body{position:relative;background:var(--white);font-family:"Lato",Arial,sans-serif;color:var(--text)}
.abs{position:absolute}
.display{font-family:"Rajdhani",Arial,sans-serif;font-weight:700;color:var(--ink);text-transform:uppercase;letter-spacing:.5px}
.section-title{position:absolute;left:0;width:1200px;text-align:center;font-size:38px;line-height:40px}
.btn{position:absolute;display:flex;align-items:center;justify-content:center;background:var(--orange);color:var(--white);font-size:10px;font-weight:700;text-transform:uppercase;letter-spacing:.4px}
.photo{position:absolute}
.body-copy{font-size:12.5px;line-height:19px;color:var(--muted)}

/* header */
.topbar{left:785px;top:0;width:415px;height:29px;background:var(--orange);clip-path:polygon(14px 0,100% 0,100% 100%,0 100%);color:var(--white);font-size:11px;display:flex;align-items:center;gap:22px;padding-left:30px}
.brand{left:93px;top:18px;display:flex;align-items:center;gap:10px}
.brand-mark{width:34px;height:34px;border-radius:50%;background:var(--orange)}
.brand-name{font-family:"Rajdhani",sans-serif;font-weight:700;font-size:24px;color:var(--orange);text-transform:uppercase;letter-spacing:.5px}
.nav{top:46px;left:0;font-size:11px;color:var(--ink);text-transform:uppercase}
.nav span{position:absolute;white-space:nowrap}
.nav .active{color:var(--orange)}

/* hero */
.hero{left:0;top:73px;width:1200px;height:529px;background:linear-gradient(180deg,#8fa08a 0%,#4d7a3a 35%,#5d6e2f 60%,#7a3a2a 80%,#4a6a2c 100%)}
.hero-cut{left:0;top:565px;width:360px;height:38px;background:var(--white);clip-path:polygon(0 0,100% 0,82% 100%,0 100%)}
.hero-kicker{left:669px;top:272px;font-size:28px;color:var(--white);font-weight:600}
.hero-title{left:669px;top:306px;font-size:44px;line-height:50px;color:var(--white)}

/* welcome */
.welcome-kicker{left:93px;top:745px;font-size:15px;color:var(--ink);text-transform:uppercase}
.welcome-title{left:93px;top:770px;font-size:38px}
.welcome-copy{left:93px;top:820px;width:510px}
.welcome-photo{left:668px;top:629px;width:439px;height:460px;border-radius:0 0 220px 220px;background:linear-gradient(180deg,#e9eef2 0%,#b9c6a6 30%,#5f7f48 60%,#3f5a66 78%,#44632f 100%)}

/* applications */
.apps{left:0;top:1149px;width:1200px;height:296px;background:var(--soft)}
.kicker{position:absolute;left:0;width:1200px;text-align:center;font-size:14px;text-transform:uppercase;color:var(--ink)}
.app{position:absolute;top:1278px;width:220px;text-align:center}
.app-icon{width:92px;height:92px;margin:0 auto;border-radius:50%;background:var(--orange);border:6px solid var(--green);display:flex;align-items:center;justify-content:center}
.app-label{margin-top:18px;font-size:21px;font-weight:700;color:var(--ink);text-transform:uppercase}

/* technology */
.tech{left:0;top:1499px;width:1200px;height:905px;background:#f8f8f8}
.card-title{position:absolute;font-size:17px;color:var(--ink)}
.card-copy{position:absolute;width:310px}
.arrow-round{position:absolute;width:34px;height:34px;border-radius:50%;background:var(--white);border:1px solid var(--line);display:flex;align-items:center;justify-content:center}
.member{position:absolute;top:2025px;width:239px;height:264px;border-radius:120px 120px 0 0}
.member-name{position:absolute;top:2306px;width:239px;text-align:center;font-size:15px;color:var(--ink);text-transform:uppercase}
.member-role{position:absolute;top:2332px;width:239px;text-align:center;font-size:10.5px;color:var(--ink)}

/* feature */
.feature{left:0;top:2404px;width:1200px;height:744px;background:linear-gradient(135deg,#2c2c2c 0%,#121212 100%)}
.feat-title{position:absolute;font-family:"Rajdhani",sans-serif;font-weight:700;font-size:26px;line-height:30px;color:var(--white);text-transform:uppercase;letter-spacing:.5px;white-space:nowrap}
.feat-sub{position:absolute;font-size:17px;font-weight:400;line-height:22px;color:var(--white);white-space:nowrap}
.feat-copy{position:absolute;font-size:12.5px;line-height:19px;color:#9a9a9a}
.play{left:472px;top:2920px;width:44px;height:44px;border-radius:50%;border:2px solid var(--white);background:rgba(255,255,255,.25);display:flex;align-items:center;justify-content:center}

/* news */
.news-date{position:absolute;top:3482px;font-size:10.5px;color:var(--ink)}
.news-title{position:absolute;top:3507px;font-size:17px;color:var(--ink)}

/* banner */
.banner{left:0;top:3703px;width:1200px;height:200px;background:var(--orange)}
.banner-kicker{left:0;top:3744px;width:1200px;text-align:center;color:var(--white);font-size:13px}
.banner-title{left:0;top:3766px;width:1200px;text-align:center;font-size:38px;color:var(--white)}
.btn-green{left:529px;top:3823px;width:139px;height:37px;background:var(--green)}

/* about */
.col{position:absolute;top:4024px;width:330px}
.col h5{font-family:"Rajdhani",sans-serif;font-weight:600;font-size:21px;color:var(--ink);text-transform:uppercase}
.col .rule{width:170px;height:1px;background:var(--line);margin:6px 0 10px}
.col p{font-size:12.5px;line-height:19px;color:var(--muted)}
.col strong{display:block;margin-top:10px;font-size:13px;color:var(--ink)}
.partners{left:93px;top:4237px;width:1014px;height:78px;border-top:1px solid var(--line);border-bottom:1px solid var(--line)}
.partner{position:absolute;top:4262px;width:130px;height:26px;border-radius:4px;background:#cfcfcf}

/* footer */
.footer{left:0;top:4365px;width:1200px;height:329px;background:var(--dark)}
.f-head{position:absolute;top:4406px;font-size:15px;color:var(--white);text-transform:uppercase;font-family:"Rajdhani",sans-serif;font-weight:600}
.f-list{position:absolute;top:4440px;font-size:11px;line-height:27px;color:#a0a0a0;list-style:none}
.f-info{position:absolute;font-size:11px;color:#a0a0a0;display:flex;gap:6px;line-height:15px}
.field{position:absolute;border:1px solid #555;font-size:10px;color:#cfcfcf;padding:8px 8px}
.send{left:1029px;top:4560px;width:78px;height:31px}
.social{left:588px;top:4606px;width:24px;height:24px;border-radius:50%;background:var(--white)}
.copyright{left:0;top:4644px;width:1200px;text-align:center;font-size:10.5px;color:#cfcfcf}
.copyright b{color:var(--orange);font-weight:400}
</style>
</head>
<body>

<!-- header -->
<div class="abs topbar">
  <span>&#9990; +31 6 55501234</span>
  <span>&#9993; info@valteradrones-example.com</span>
  <span>En &#709;</span>
</div>
<div class="abs brand"><span class="brand-mark"></span><span class="brand-name">Valtera Drones</span></div>
<nav class="abs nav">
  <span class="active" style="left:491px">Home</span>
  <span style="left:567px">Crop Monitoring</span>
  <span style="left:710px">Technology</span>
  <span style="left:826px">About</span>
  <span style="left:907px">News&amp;Downloads</span>
  <span style="left:1058px">Contact</span>
</nav>

<!-- hero -->
<div class="abs hero" role="img" aria-label="Orange drone flying over a colourful flower greenhouse with laser guide lines"></div>
<div class="abs hero-cut"></div>
<svg class="abs" style="left:250px;top:576px" width="64" height="14" viewBox="0 0 64 14">
  <path d="M2 7h24M2 7l5-4M2 7l5 4M38 7h24M62 7l-5-4M62 7l-5 4" stroke="#1e1e1e" stroke-width="1.6" fill="none"/>
</svg>
<div class="abs hero-kicker display" style="color:#fff;font-weight:600">Valtera Drones</div>
<div class="abs hero-title display" style="color:#fff">Enables Aerial Data<br>Collection</div>

<!-- welcome -->
<div class="abs welcome-kicker">Welcome to</div>
<h1 class="abs welcome-title display">Valtera Drones</h1>
<p class="abs welcome-copy body-copy">Valtera Drones has developed a unique autonomous drone system that is able to fly and navigate in a greenhouse without manual interference. Based on a flight plan the drone follows the right coordinates in the greenhouse, day or night, collecting high accurate data. Data is being interpreted by Artificial Intelligence software resulting in crop improvement information. The focus is the following four customer pains: Development, Plant stress, Growth and Diseases.</p>
<div class="btn" style="left:93px;top:967px;width:103px;height:36px">Read More</div>
<div class="photo welcome-photo" role="img" aria-label="Orange drone hovering above farmland and a lake"></div>

<!-- applications -->
<div class="abs apps"></div>
<div class="kicker" style="top:1194px">Crop Monitoring</div>
<h2 class="section-title display" style="top:1218px">Applications</h2>
<div class="app" style="left:109px">
  <div class="app-icon"><svg width="40" height="40" viewBox="0 0 40 40" fill="none" stroke="#fff" stroke-width="2.4"><path d="M20 34V18M20 22c-8 0-11-6-11-11 6 0 11 4 11 11zM20 19c0-7 5-11 11-11 0 6-4 11-11 11zM6 34h28"/></svg></div>
  <div class="app-label">Growth</div>
</div>
<div class="app" style="left:364px">
  <div class="app-icon"><svg width="40" height="40" viewBox="0 0 40 40" fill="none" stroke="#fff" stroke-width="2.4"><path d="M12 34v-8c-4-3-5-7-5-11a13 13 0 0 1 26 0c0 3-1 6-3 8v11M20 10v10M15 15l5 5 5-5"/></svg></div>
  <div class="app-label">Stress</div>
</div>
<div class="app" style="left:616px">
  <div class="app-icon"><svg width="40" height="40" viewBox="0 0 40 40" fill="none" stroke="#fff" stroke-width="2.4"><path d="M20 4l13 5v10c0 9-6 14-13 17-7-3-13-8-13-17V9zM20 28v-9M20 21c-5 0-7-3-7-7 4 0 7 3 7 7zM20 19c0-4 3-7 7-7 0 4-3 7-7 7z"/></svg></div>
  <div class="app-label">Development</div>
</div>
<div class="app" style="left:869px">
  <div class="app-icon"><svg width="40" height="40" viewBox="0 0 40 40" fill="#fff"><circle cx="20" cy="20" r="9"/><g stroke="#fff" stroke-width="2.4"><path d="M20 4v7M20 29v7M4 20h7M29 20h7M9 9l5 5M26 26l5 5M31 9l-5 5M14 26l-5 5"/></g><circle cx="17" cy="18" r="2" fill="#f78f20"/><circle cx="23" cy="23" r="1.6" fill="#f78f20"/></svg></div>
  <div class="app-label">Diseases</div>
</div>

<!-- technology -->
<div class="abs tech"></div>
<h2 class="section-title display" style="top:1502px">Technology</h2>
<div class="photo" style="left:93px;top:1561px;width:325px;height:199px;background:linear-gradient(180deg,#8fb86a,#3d5a2c)" role="img" aria-label="Hands holding a tablet with drone footage in front of trees"></div>
<div class="photo" style="left:438px;top:1561px;width:325px;height:199px;background:linear-gradient(135deg,#a5874a,#6e7a3a 50%,#b39a5c)" role="img" aria-label="Aerial view of farm fields and a tree line"></div>
<div class="photo" style="left:781px;top:1561px;width:325px;height:199px;background:linear-gradient(180deg,#a9b7c6,#c9c7bb 45%,#4f6a3c)" role="img" aria-label="Wide landscape of fields under a cloudy sky"></div>
<div class="card-title" style="left:93px;top:1772px">Aerial Data Collection</div>
<div class="card-title" style="left:438px;top:1772px">Artificial intelligence</div>
<div class="card-title" style="left:781px;top:1772px">Free Data Sets</div>
<p class="card-copy body-copy" style="left:93px;top:1803px">Sed ut perspiciatis unde omnis iste natus error sit voluptatem accusantium doloremque laudantium totam rem</p>
<p class="card-copy body-copy" style="left:438px;top:1803px">Sed ut perspiciatis unde omnis iste natus error sit voluptatem accusantium doloremque laudantium totam rem</p>
<p class="card-copy body-copy" style="left:781px;top:1803px">Sed ut perspiciatis unde omnis iste natus error sit voluptatem accusantium doloremque laudantium totam rem</p>
<div class="btn" style="left:93px;top:1871px;width:95px;height:32px">Read More</div>
<div class="btn" style="left:438px;top:1871px;width:95px;height:32px">Read More</div>
<div class="btn" style="left:781px;top:1871px;width:95px;height:32px">Read More</div>

<!-- team -->
<h2 class="section-title display" style="top:1961px">Meet Our Team</h2>
<div class="arrow-round" style="left:30px;top:2141px"><svg width="10" height="10" viewBox="0 0 10 10"><path d="M6 2L3 5l3 3" stroke="#333" fill="none" stroke-width="1.4"/></svg></div>
<div class="arrow-round" style="left:1136px;top:2141px"><svg width="10" height="10" viewBox="0 0 10 10"><path d="M4 2l3 3-3 3" stroke="#333" fill="none" stroke-width="1.4"/></svg></div>
<div class="member" style="left:93px;background:linear-gradient(180deg,#dcdcdc,#a7774a)" role="img" aria-label="Portrait of team member, farmer in a hat"></div>
<div class="member" style="left:352px;background:linear-gradient(180deg,#d6d6d6,#5a4a40)" role="img" aria-label="Portrait of team member, consultant"></div>
<div class="member" style="left:611px;background:linear-gradient(180deg,#cfcfcf,#4a6a8a)" role="img" aria-label="Portrait of team member, farmer"></div>
<div class="member" style="left:868px;background:linear-gradient(180deg,#8a8a80,#4a5a3a)" role="img" aria-label="Portrait of team member, farmer"></div>
<div class="member-name" style="left:93px">Mr. Aren Tolvik</div>
<div class="member-name" style="left:352px">Mr. Joren Baskel</div>
<div class="member-name" style="left:611px">Mr. Idris Valmont</div>
<div class="member-name" style="left:868px">Mr. Lukas Ferrend</div>
<div class="member-role" style="left:93px">Farmer</div>
<div class="member-role" style="left:352px">Consultant</div>
<div class="member-role" style="left:611px">Farmer</div>
<div class="member-role" style="left:868px">Farmer</div>

<!-- feature -->
<div class="abs feature"></div>
<h3 class="feat-title" style="left:93px;top:2500px">Greenhouse Drone</h3>
<h4 class="feat-sub" style="left:93px;top:2537px">Crop monitoring by aerial data-collection</h4>
<p class="feat-copy" style="left:93px;top:2570px;width:340px">Using drones in greenhouses opens up opportunities to optimize the growth process. With the Valtera drone a wide variety of data can be collected, which is analyzed using advanced Artificial Intelligence algorithms.</p>
<div class="btn" style="left:93px;top:2683px;width:95px;height:31px">Read More</div>
<div class="photo" style="left:445px;top:2459px;width:310px;height:304px;background:linear-gradient(180deg,#c9ccd0 0%,#d9c7a8 55%,#e8a24a 70%,#5a6a3a 85%,#3a4a2a 100%)" role="img" aria-label="Drone flying over a field at sunset"></div>
<div class="photo" style="left:233px;top:2787px;width:522px;height:305px;background:linear-gradient(180deg,#c8ccd0 0%,#8e9a8a 40%,#5b8a3a 75%,#466a2c 100%)" role="img" aria-label="Video still of an orange drone inside a large greenhouse"></div>
<div class="abs play"><svg width="14" height="16" viewBox="0 0 14 16"><path d="M2 1l11 7-11 7z" fill="#fff"/></svg></div>
<h3 class="feat-title" style="left:772px;top:2830px">Seed Germination Ratio</h3>
<p class="feat-copy" style="left:772px;top:2871px;width:330px">Valtera Drones is specialist in aerial data-collection and crop monitoring in horticulture. The drone flies autonomous in greenhouses, collects crop data and artificial intelligence software interpreted the data.</p>
<div class="btn" style="left:776px;top:2964px;width:92px;height:31px">Read More</div>

<!-- news -->
<h2 class="section-title display" style="top:3203px">Recent News</h2>
<div class="arrow-round" style="left:30px;top:3354px"><svg width="10" height="10" viewBox="0 0 10 10"><path d="M6 2L3 5l3 3" stroke="#333" fill="none" stroke-width="1.4"/></svg></div>
<div class="arrow-round" style="left:1136px;top:3354px"><svg width="10" height="10" viewBox="0 0 10 10"><path d="M4 2l3 3-3 3" stroke="#333" fill="none" stroke-width="1.4"/></svg></div>
<div class="photo" style="left:93px;top:3270px;width:325px;height:199px;background:linear-gradient(180deg,#6a7888 0%,#c8a070 60%,#7a5a2a 100%)" role="img" aria-label="Drone above a wheat field at dusk"></div>
<div class="photo" style="left:438px;top:3270px;width:325px;height:199px;background:linear-gradient(180deg,#e6ecef 0%,#8aa76a 45%,#5f8a3a 100%)" role="img" aria-label="Spraying drone over a rice paddy"></div>
<div class="photo" style="left:781px;top:3270px;width:325px;height:199px;background:linear-gradient(135deg,#c8b03a,#7a8a3a 50%,#d6c04a)" role="img" aria-label="Aerial view of a road crossing yellow fields"></div>
<div class="news-date" style="left:93px">15 July, 2020</div>
<div class="news-date" style="left:438px">15 July, 2020</div>
<div class="news-date" style="left:781px">15 July, 2020</div>
<div class="news-title" style="left:93px">Duis aute irure dolor in Reprehenderit</div>
<div class="news-title" style="left:438px">Duis aute irure dolor in Reprehenderit</div>
<div class="news-title" style="left:781px">Duis aute irure dolor in Reprehenderit</div>
<p class="card-copy body-copy" style="left:93px;top:3538px">Sed ut perspiciatis unde omnis iste natus error sit voluptatem accusantium doloremque laudantium totam rem</p>
<p class="card-copy body-copy" style="left:438px;top:3538px">Sed ut perspiciatis unde omnis iste natus error sit voluptatem accusantium doloremque laudantium totam rem</p>
<p class="card-copy body-copy" style="left:781px;top:3538px">Sed ut perspiciatis unde omnis iste natus error sit voluptatem accusantium doloremque laudantium totam rem</p>
<div class="btn" style="left:93px;top:3606px;width:95px;height:33px">Read More</div>
<div class="btn" style="left:438px;top:3606px;width:95px;height:33px">Read More</div>
<div class="btn" style="left:781px;top:3606px;width:95px;height:33px">Read More</div>

<!-- banner -->
<div class="abs banner"></div>
<div class="abs banner-kicker">FINIBUS BONORUM</div>
<div class="abs banner-title display" style="color:#fff">Nor Again Is There Anyone Who Loves Or Pursues</div>
<div class="btn btn-green">Download Now</div>

<!-- about -->
<h2 class="section-title display" style="top:3960px">About Us</h2>
<div class="col" style="left:93px"><h5>Our Vision</h5><div class="rule"></div><p>Our current and successful application is germination counting. Thousands of seedling trays are monitored within the shortest possible time. The result is an exact insight of the seedling rate and crop development status.</p></div>
<div class="col" style="left:452px"><h5>Company</h5><div class="rule"></div><p>Our current and successful application is germination counting. Thousands of seedling trays are monitored within the shortest possible time. The result is an exact insight of the seedling rate and crop development status.</p></div>
<div class="col" style="left:812px"><h5>Testimonials</h5><div class="rule"></div><p>Sed ut perspiciatis unde omnis iste natus error sit voluptatem accusantium doloremque laudantium, totam rem aperiam, eaque ipsa quae ab illo inventore...</p><strong>Mr. Aren Tolvik</strong></div>
<div class="abs partners"></div>
<div class="partner" style="left:95px"></div>
<div class="partner" style="left:355px"></div>
<div class="partner" style="left:595px"></div>
<div class="partner" style="left:805px"></div>
<div class="partner" style="left:1010px;width:96px"></div>

<!-- footer -->
<div class="abs footer"></div>
<div class="f-head" style="left:93px">Quick Links</div>
<div class="f-head" style="left:301px">Markets</div>
<div class="f-head" style="left:474px">Contacts</div>
<div class="f-head" style="left:722px">Send a Message</div>
<ul class="f-list" style="left:93px"><li>Home</li><li>Crop Monitoring</li><li>Technology</li><li>About Us</li><li>News &amp; Downloads</li><li>Contact Us</li></ul>
<ul class="f-list" style="left:301px"><li>Breeding</li><li>Young plant</li><li>Potplants</li><li>Cutflowers</li><li>Vegetables</li><li>Soft fruit</li></ul>
<div class="f-info" style="left:474px;top:4444px"><svg width="9" height="12" viewBox="0 0 9 12"><path d="M4.5 0A4.5 4.5 0 0 0 0 4.5C0 8 4.5 12 4.5 12S9 8 9 4.5A4.5 4.5 0 0 0 4.5 0z" fill="#f78f20"/><circle cx="4.5" cy="4.5" r="1.6" fill="#1b1b1b"/></svg><span>Veldweg 14B,<br>1234AB, Harderbroek</span></div>
<div class="f-info" style="left:474px;top:4519px"><svg width="10" height="12" viewBox="0 0 10 12"><path d="M2 0l2 3-1.2 1.4c.6 1.6 1.6 2.8 3 3.6L7 7l3 2-1 2.5C4 11 1 7 0 1.5z" fill="#f78f20"/></svg><span>+31 6 55501234</span></div>
<div class="f-info" style="left:474px;top:4563px"><svg width="11" height="9" viewBox="0 0 11 9"><rect width="11" height="9" fill="#f78f20"/><path d="M0 0l5.5 5L11 0" stroke="#1b1b1b" fill="none"/></svg><span>info@valteradrones-example.com</span></div>
<div class="field" style="left:722px;top:4443px;width:190px;height:33px">Name:</div>
<div class="field" style="left:722px;top:4481px;width:190px;height:33px">Email:</div>
<div class="field" style="left:722px;top:4518px;width:190px;height:35px">Phone:</div>
<div class="field" style="left:916px;top:4443px;width:191px;height:110px">Message:</div>
<div class="btn send">Send</div>
<div class="abs social"></div>
<div class="abs copyright">COPYRIGHT &copy; 2020 <b>VALTERA DRONES</b>. ALL RIGHTS RESERVED.</div>

</body>
</html>
```